Ridgemont Business Card Redesign

Using the current logo/tagline lock-up and icon, redesign the Ridgemont business card to better show the tagline and improve the layout to give the card a more timely design and a classic, sophisticated look. See attached Project Brief for more detail.

```html
<!DOCTYPE html>
<html lang="en">
<head>
<meta charset="utf-8">
<title>Ridgemont Capital – Business Card</title>
<link href="https://fonts.googleapis.com/css2?family=Montserrat:wght@400;500;600&display=swap" rel="stylesheet">
<style>
  :root {
    --backdrop: #5e5e5e;
    --card: #f7f7f7;
    --brand-blue: #1a6fb0;
    --text-grey: #6e6e6e;
    --logo-grey: #5a5a5a;
  }
  * { margin: 0; padding: 0; box-sizing: border-box; }
  html, body { width: 1200px; height: 900px; overflow: hidden; }
  body {
    background: var(--backdrop);
    font-family: "Montserrat", Arial, sans-serif;
    position: relative;
  }
  .business-card {
    position: absolute;
    left: 75px; top: 150px;
    width: 1050px; height: 600px;
    background: var(--card);
    border-radius: 4px;
    box-shadow: 0 10px 30px rgba(0,0,0,.35);
  }
  .holder { position: absolute; left: 110px; top: 120px; }
  .holder-name {
    color: var(--brand-blue);
    font-weight: 600;
    font-size: 42px;
    letter-spacing: .5px;
  }
  .holder-title {
    color: var(--text-grey);
    font-size: 27px;
    line-height: 1.2;
    margin-top: 8px;
  }
  .address {
    position: absolute; left: 110px; top: 318px;
    color: var(--text-grey);
    font-size: 23px;
    line-height: 1.3;
  }
  .contact-list {
    position: absolute; left: 110px; top: 400px;
    list-style: none;
  }
  .contact-item {
    display: flex; align-items: center;
    height: 40px;
    color: var(--text-grey);
    font-size: 23px;
  }
  .contact-icon {
    width: 24px; height: 24px;
    margin-right: 26px;
    fill: var(--brand-blue);
  }
  .logo-lockup {
    position: absolute; left: 640px; top: 330px;
    display: flex; align-items: center;
  }
  .logo-dot {
    width: 70px; height: 70px;
    border-radius: 50%;
    background: var(--brand-blue);
    margin-right: 22px;
  }
  .logo-name {
    color: var(--logo-grey);
    font-weight: 500;
    font-size: 34px;
    letter-spacing: 3px;
    text-transform: uppercase;
    line-height: 1.1;
  }
  .logo-tagline {
    color: var(--brand-blue);
    font-size: 14px;
    letter-spacing: 2px;
    text-transform: uppercase;
    border-top: 1px solid var(--logo-grey);
    padding-top: 6px;
    margin-top: 8px;
  }
</style>
</head>
<body>
  <main class="business-card">
    <section class="holder">
      <h1 class="holder-name">Daniel R. Whitford</h1>
      <p class="holder-title">Principal &amp;<br>Chief Marketing Officer</p>
    </section>

    <p class="address">41 Alder Crest Road<br>Suite 210 - Norwalk, CT 06851</p>

    <ul class="contact-list">
      <li class="contact-item">
        <svg class="contact-icon" viewBox="0 0 24 24"><path d="M7 1h10a2 2 0 0 1 2 2v18a2 2 0 0 1-2 2H7a2 2 0 0 1-2-2V3a2 2 0 0 1 2-2zm0 3v14h10V4zm5 15.5a1.2 1.2 0 1 0 0 2.4 1.2 1.2 0 0 0 0-2.4z"/></svg>
        (555) 214-3087
      </li>
      <li class="contact-item">
        <svg class="contact-icon" viewBox="0 0 24 24"><path d="M6.6 10.8a15 15 0 0 0 6.6 6.6l2.2-2.2a1 1 0 0 1 1-.25 11.4 11.4 0 0 0 3.6.57 1 1 0 0 1 1 1V20a1 1 0 0 1-1 1A17 17 0 0 1 3 4a1 1 0 0 1 1-1h3.5a1 1 0 0 1 1 1c0 1.25.2 2.45.57 3.6a1 1 0 0 1-.25 1z"/></svg>
        (555) 618-2045
      </li>
      <li class="contact-item">
        <svg class="contact-icon" viewBox="0 0 24 24"><path d="M2 5h20v14H2zm2 2v.4l8 5.3 8-5.3V7zm0 2.8V17h16V9.8l-8 5.3z"/></svg>
        dwhitford@ridgemontcapital.com
      </li>
      <li class="contact-item">
        <svg class="contact-icon" viewBox="0 0 24 24"><path d="M12 2a10 10 0 1 0 0 20 10 10 0 0 0 0-20zm6.9 6h-3a15 15 0 0 0-1.3-3.7A8 8 0 0 1 18.9 8zM12 4c.8 1.1 1.5 2.5 1.9 4h-3.8c.4-1.5 1.1-2.9 1.9-4zM4.3 14a8 8 0 0 1 0-4h3.4a16 16 0 0 0 0 4zm.8 2h3a15 15 0 0 0 1.3 3.7A8 8 0 0 1 5.1 16zm3-8h-3a8 8 0 0 1 4.3-3.7A15 15 0 0 0 8.1 8zM12 20c-.8-1.1-1.5-2.5-1.9-4h3.8c-.4 1.5-1.1 2.9-1.9 4zm2.3-6H9.7a14 14 0 0 1 0-4h4.6a14 14 0 0 1 0 4zm.3 5.7a15 15 0 0 0 1.3-3.7h3a8 8 0 0 1-4.3 3.7zM16.3 14a16 16 0 0 0 0-4h3.4a8 8 0 0 1 0 4z"/></svg>
        www.ridgemontcapital.com
      </li>
    </ul>

    <div class="logo-lockup">
      <span class="logo-dot" aria-hidden="true"></span>
      <div>
        <p class="logo-name">Ridgemont<br>Capital</p>
        <p class="logo-tagline">Non-Control Growth Capital</p>
      </div>
    </div>
  </main>
</body>
</html>
```